BANNER FOR ONLINE CABINET COMPANY MAIN PAGE

Need 3 different banners for the main page. We are online platform for ordering cabinets, parts etc. online.
Website: bordaline.ca
A place where the banner will be placed: https://view.pelmoraclip.com/qTR7WkVbNHEa4
Banner size: 1344x399 pixels
****Clients should get the main point that they can order everything online through the website.

Industry/Entity Type

online cabinets and parts ordering

Requirements
Must have
• online ordering icons, vexaphone, laptop, desktop pc - so clients get an idea that this is web based service to order cabinets

```html
<!DOCTYPE html>
<html lang="en">
<head>
<meta charset="utf-8">
<title>Bordaline – Main Page Banners</title>
<link rel="stylesheet" href="https://fonts.googleapis.com/css2?family=Roboto:ital,wght@0,300;0,400;0,500;0,700;0,900;1,700;1,900&display=swap">
<style>
:root{
  --stage:#2b323a;
  --topbar:#26292d;
  --band:#e6e6e6;
  --ink:#111;
  --muted:#555;
  --blue:#3a8fdd;
  --blue-deep:#1f6fc4;
  --orange:#f7a21b;
  --green:#2fb34a;
  --white:#fff;
}
*{box-sizing:border-box;margin:0;padding:0}
html,body{width:1200px;height:3114px;overflow:hidden}
body{background:var(--stage);font-family:"Roboto",Arial,sans-serif;position:relative;color:var(--ink)}

/* ---------- site preview ---------- */
.site{position:absolute;left:0;width:1200px;height:552px;background:var(--white);overflow:hidden}
.topbar{height:31px;background:var(--topbar);display:flex;align-items:center;padding:0 26px;color:var(--white);font-size:7.5px;white-space:nowrap}
.brand{font-weight:700;font-size:12px;display:flex;align-items:center;gap:4px;padding-right:10px;border-right:1px solid #777;height:18px}
.brand .dot{width:6px;height:6px;background:#e23b30;display:inline-block}
.tagline{margin-left:12px}
.callbox{margin-left:20px;background:#000;padding:4px 8px;display:flex;gap:12px}
.nav{margin-left:auto;display:flex;align-items:center;gap:15px;font-weight:500}
.nav .order{background:var(--green);border-radius:9px;padding:3px 8px}
.nav svg{display:block}
.title-band{height:57px;background:var(--band);text-align:center;padding-top:4px}
.title-band h1{font-size:19px;font-weight:700;letter-spacing:.4px}
.title-band p{font-size:13px;color:var(--muted);margin-top:5px}
.site .hero{position:absolute;top:88px;left:0}
.pager{position:absolute;top:454px;left:551px;display:flex;gap:7px}
.pager i{width:8px;height:6px;background:#ccc;display:block}
.pager i.on{background:var(--orange)}
.site h2{position:absolute;top:482px;width:100%;text-align:center;font-size:19px;font-weight:700;letter-spacing:.3px}
.chat{position:absolute;right:10px;bottom:0;background:var(--topbar);color:var(--white);font-size:7.5px;padding:6px 22px 6px 12px;border-radius:6px 6px 0 0;white-space:nowrap}
.chat:after{content:"";position:absolute;right:-4px;top:0;width:14px;height:14px;border-radius:50%;background:var(--green)}

/* ---------- hero banner ---------- */
.hero{width:1200px;height:363px;overflow:hidden;position:relative}
.photo{position:absolute;inset:0}
.photo-fridge{background:linear-gradient(90deg,#d9d9d9 0%,#b8b8b8 25%,#efefef 55%,#f4f4f4 80%,#e2e2e2 100%)}
.photo-white{background:linear-gradient(90deg,#d5d8cf 0%,#eeeeee 20%,#f3f3f3 55%,#c9c9c9 80%,#ededed 100%)}
.photo-dark{background:linear-gradient(180deg,#7d746d 0%,#9a928b 55%,#e8e8e8 68%,#f4f4f4 100%)}
.hero svg.shapes{position:absolute;inset:0}
.hero .copy{position:absolute;text-align:center;color:var(--white);white-space:nowrap}
.cta{position:absolute;height:40px;background:var(--orange);transform:skewX(-14deg);display:flex;align-items:center;justify-content:center}
.cta span{transform:skewX(14deg);color:var(--white);font-weight:700;font-size:16px;letter-spacing:1.5px;white-space:nowrap}
.slides{position:absolute;right:52px;top:156px;display:flex;flex-direction:column;gap:11px}
.slides i{width:8px;height:8px;background:var(--white);transform:rotate(45deg);display:block}
.slides i.on{background:var(--blue-deep)}

/* online ordering devices */
.devices{position:absolute;display:flex;align-items:flex-end;gap:12px}
.devices svg{display:block}
.hero-a .devices{left:456px;top:300px;color:var(--white)}
.hero-b .devices{left:445px;top:252px;color:var(--blue-deep)}
.hero-c .devices{left:300px;top:118px;color:var(--white)}

.hero-a .copy{left:440px;width:390px;top:98px}
.hero-a h3{font-size:38px;font-weight:900;font-style:italic}
.hero-a p{font-size:14.5px;line-height:20px;margin-top:8px;font-weight:300}
.hero-a .cta{left:497px;top:230px;width:208px}

.hero-b .copy{left:208px;top:70px;text-align:left;color:var(--ink)}
.hero-b h3{font-size:41px;font-weight:900;line-height:40px}
.hero-b p{font-size:14.5px;line-height:20px;margin-top:22px;font-weight:300;color:#222}
.hero-b .cta{left:208px;top:250px;width:211px}

.hero-c .copy{left:454px;width:300px;top:94px;color:var(--ink)}
.hero-c h3{font-size:31px;font-weight:900;line-height:27px}
.hero-c p{font-size:14px;line-height:19px;margin-top:12px;font-weight:300;color:#333}
.hero-c .cta{left:501px;top:233px;width:212px}

/* ---------- standalone banners ---------- */
.banner{position:absolute;left:138px;width:925px;height:280px;overflow:hidden}
.banner .hero{transform:scale(.7708);transform-origin:0 0}
</style>
</head>
<body>

<svg width="0" height="0" style="position:absolute" aria-hidden="true">
  <symbol id="icon-phone" viewBox="0 0 16 26"><rect x="1" y="1" width="14" height="24" rx="2.5" fill="none" stroke="currentColor" stroke-width="1.8"/><line x1="6" y1="21" x2="10" y2="21" stroke="currentColor" stroke-width="1.8"/></symbol>
  <symbol id="icon-laptop" viewBox="0 0 36 24"><rect x="5" y="1" width="26" height="17" rx="1.5" fill="none" stroke="currentColor" stroke-width="1.8"/><path d="M1 22h34" stroke="currentColor" stroke-width="2.4" stroke-linecap="round"/></symbol>
  <symbol id="icon-desktop" viewBox="0 0 34 30"><rect x="1" y="1" width="32" height="21" rx="1.5" fill="none" stroke="currentColor" stroke-width="1.8"/><path d="M17 22v5M10 28h14" stroke="currentColor" stroke-width="1.8"/></symbol>
</svg>

<!-- ===== Preview 1 ===== -->
<section class="site" style="top:0">
  <header class="topbar">
    <div class="brand">Bordaline<span class="dot"></span></div>
    <span class="tagline">Get the size you need!</span>
    <div class="callbox"><span>&#9990; Call us (555) 014 2290</span><span>&#9719; Mon-Fri 8AM - 4.30PM</span></div>
    <nav class="nav"><span>CAD</span><span class="order">ORDER NOW</span><span>DESIGN &amp; QUOTE</span><span>SAMPLES</span><span>ABOUT</span><span>CONTACT</span><span>ARTICLES</span>
      <svg width="9" height="9" viewBox="0 0 10 10"><circle cx="4" cy="4" r="3" fill="none" stroke="#fff"/><path d="M6 6l3 3" stroke="#fff"/></svg><b style="font-size:13px">?</b>
      <svg width="11" height="11" viewBox="0 0 12 12"><circle cx="6" cy="4" r="2.5" fill="none" stroke="#fff"/><path d="M1 11c1-3 9-3 10 0" fill="none" stroke="#fff"/></svg>
      <svg width="12" height="11" viewBox="0 0 12 11"><path d="M0 1h2l2 6h6l1-4H3" fill="none" stroke="#fff"/><circle cx="5" cy="9.5" r="1" fill="#fff"/><circle cx="9" cy="9.5" r="1" fill="#fff"/></svg></nav>
  </header>
  <div class="title-band"><h1>THE FIRST ONLINE CUSTOM CABINET’S MANUFACTURER</h1><p>Order custom cabinets online with instant price calculator. No hidden fees, top quality warranty.</p></div>
  <div class="hero hero-a">
    <div class="photo photo-fridge" role="img" aria-label="Bright white kitchen with stainless fridge and wine rack"></div>
    <svg class="shapes" viewBox="0 0 1200 363" preserveAspectRatio="none"><polygon points="465,0 906,0 750,363 378,363" fill="#3a8fdd" opacity=".92"/><polyline points="195,353 365,353 410,160" fill="none" stroke="#1f6fc4" stroke-width="3"/><polyline points="1040,27 905,27 860,180" fill="none" stroke="#f7a21b" stroke-width="3"/></svg>
    <div class="copy"><h3>MDF Shaker Doors</h3><p>Timeless &amp; Most Popular Style of Kitchen Doors<br>- Painted or Ready for Painting Options<br>- Short Lead Time</p></div>
    <div class="cta"><span>CHECK THE PRICE</span></div>
    <div class="devices" role="img" aria-label="Order online from phone, laptop or desktop"><svg width="16" height="26"><use href="#icon-phone"/></svg><svg width="36" height="24"><use href="#icon-laptop"/></svg><svg width="34" height="30"><use href="#icon-desktop"/></svg></div>
    <div class="slides"><i></i><i class="on"></i><i></i></div>
  </div>
  <div class="pager"><i></i><i></i><i></i><i></i><i class="on"></i><i></i><i></i></div>
  <h2>EASY QUOTE &amp; ORDER</h2>
  <div class="chat">Questions? Start chat, we are online!</div>
</section>

<!-- ===== Preview 2 ===== -->
<section class="site" style="top:627px">
  <header class="topbar">
    <div class="brand">Bordaline<span class="dot"></span></div>
    <span class="tagline">Get the size you need!</span>
    <div class="callbox"><span>&#9990; Call us (555) 014 2290</span><span>&#9719; Mon-Fri 8AM - 4.30PM</span></div>
    <nav class="nav"><span>CAD</span><span class="order">ORDER NOW</span><span>DESIGN &amp; QUOTE</span><span>SAMPLES</span><span>ABOUT</span><span>CONTACT</span><span>ARTICLES</span>
      <svg width="9" height="9" viewBox="0 0 10 10"><circle cx="4" cy="4" r="3" fill="none" stroke="#fff"/><path d="M6 6l3 3" stroke="#fff"/></svg><b style="font-size:13px">?</b>
      <svg width="11" height="11" viewBox="0 0 12 12"><circle cx="6" cy="4" r="2.5" fill="none" stroke="#fff"/><path d="M1 11c1-3 9-3 10 0" fill="none" stroke="#fff"/></svg>
      <svg width="12" height="11" viewBox="0 0 12 11"><path d="M0 1h2l2 6h6l1-4H3" fill="none" stroke="#fff"/><circle cx="5" cy="9.5" r="1" fill="#fff"/><circle cx="9" cy="9.5" r="1" fill="#fff"/></svg></nav>
  </header>
  <div class="title-band"><h1>THE FIRST ONLINE CUSTOM CABINET’S MANUFACTURER</h1><p>Order custom cabinets online with instant price calculator. No hidden fees, top quality warranty.</p></div>
  <div class="hero hero-b">
    <div class="photo photo-white" role="img" aria-label="White shaker kitchen with brass faucet, range hood and fridge"></div>
    <svg class="shapes" viewBox="0 0 1200 363"><circle cx="224" cy="112" r="75" fill="#3a8fdd"/><line x1="360" y1="102" x2="477" y2="102" stroke="#333" stroke-width="1"/><circle cx="477" cy="102" r="3" fill="#f7a21b"/></svg>
    <div class="copy"><h3>MDF<br>Shaker Doors</h3><p>Timeless &amp; Most Popular Style of Kitchen Doors<br>- Painted or Ready for Painting Options<br>- Short Lead Time</p></div>
    <div class="cta"><span>CHECK THE PRICE</span></div>
    <div class="devices" role="img" aria-label="Order online from phone, laptop or desktop"><svg width="16" height="26"><use href="#icon-phone"/></svg><svg width="36" height="24"><use href="#icon-laptop"/></svg><svg width="34" height="30"><use href="#icon-desktop"/></svg></div>
    <div class="slides" style="right:62px"><i></i><i class="on"></i><i></i></div>
  </div>
  <div class="pager"><i></i><i></i><i></i><i></i><i class="on"></i><i></i><i></i></div>
  <h2>EASY QUOTE &amp; ORDER</h2>
  <div class="chat">Questions? Start chat, we are online!</div>
</section>

<!-- ===== Preview 3 ===== -->
<section class="site" style="top:1254px">
  <header class="topbar">
    <div class="brand">Bordaline<span class="dot"></span></div>
    <span class="tagline">Get the size you need!</span>
    <div class="callbox"><span>&#9990; Call us (555) 014 2290</span><span>&#9719; Mon-Fri 8AM - 4.30PM</span></div>
    <nav class="nav"><span>CAD</span><span class="order">ORDER NOW</span><span>DESIGN &amp; QUOTE</span><span>SAMPLES</span><span>ABOUT</span><span>CONTACT</span><span>ARTICLES</span>
      <svg width="9" height="9" viewBox="0 0 10 10"><circle cx="4" cy="4" r="3" fill="none" stroke="#fff"/><path d="M6 6l3 3" stroke="#fff"/></svg><b style="font-size:13px">?</b>
      <svg width="11" height="11" viewBox="0 0 12 12"><circle cx="6" cy="4" r="2.5" fill="none" stroke="#fff"/><path d="M1 11c1-3 9-3 10 0" fill="none" stroke="#fff"/></svg>
      <svg width="12" height="11" viewBox="0 0 12 11"><path d="M0 1h2l2 6h6l1-4H3" fill="none" stroke="#fff"/><circle cx="5" cy="9.5" r="1" fill="#fff"/><circle cx="9" cy="9.5" r="1" fill="#fff"/></svg></nav>
  </header>
  <div class="title-band"><h1>THE FIRST ONLINE CUSTOM CABINET’S MANUFACTURER</h1><p>Order custom cabinets online with instant price calculator. No hidden fees, top quality warranty.</p></div>
  <div class="hero hero-c">
    <div class="photo photo-dark" role="img" aria-label="Modern kitchen with dark wood cabinets, wall ovens and pendant lights"></div>
    <svg class="shapes" viewBox="0 0 1200 363"><polygon points="624,0 810,186 624,372 438,186" fill="#3a8fdd" opacity=".85"/><polygon points="580,-10 770,180 580,370 390,180" fill="none" stroke="#3a8fdd" stroke-width="1.5"/><polygon points="604,2 780,180 604,358 428,180" fill="#fff"/><line x1="290" y1="102" x2="478" y2="102" stroke="#222"/><circle cx="478" cy="102" r="3" fill="#f7a21b"/></svg>
    <div class="copy"><h3>Kitchen<br>Cabinets</h3><p>- Wide Range of Cabinets Designs<br>- Custom Sizes<br>- Great Quality</p></div>
    <div class="cta"><span>CHECK IT OUT</span></div>
    <div class="devices" role="img" aria-label="Order online from phone, laptop or desktop"><svg width="16" height="26"><use href="#icon-phone"/></svg><svg width="36" height="24"><use href="#icon-laptop"/></svg><svg width="34" height="30"><use href="#icon-desktop"/></svg></div>
    <div class="slides"><i></i><i class="on"></i><i></i></div>
  </div>
  <div class="pager"><i></i><i></i><i></i><i></i><i class="on"></i><i></i><i></i></div>
  <h2>EASY QUOTE &amp; ORDER</h2>
  <div class="chat">Questions? Start chat, we are online!</div>
</section>

<!-- ===== Standalone banner 1 ===== -->
<div class="banner" style="top:1943px">
  <div class="hero hero-a">
    <div class="photo photo-fridge" role="img" aria-label="Bright white kitchen with stainless fridge and wine rack"></div>
    <svg class="shapes" viewBox="0 0 1200 363" preserveAspectRatio="none"><polygon points="465,0 906,0 750,363 378,363" fill="#3a8fdd" opacity=".92"/><polyline points="195,353 365,353 410,160" fill="none" stroke="#1f6fc4" stroke-width="3"/><polyline points="1040,27 905,27 860,180" fill="none" stroke="#f7a21b" stroke-width="3"/></svg>
    <div class="copy"><h3>MDF Shaker Doors</h3><p>Timeless &amp; Most Popular Style of Kitchen Doors<br>- Painted or Ready for Painting Options<br>- Short Lead Time</p></div>
    <div class="cta"><span>CHECK THE PRICE</span></div>
    <div class="devices" role="img" aria-label="Order online from phone, laptop or desktop"><svg width="16" height="26"><use href="#icon-phone"/></svg><svg width="36" height="24"><use href="#icon-laptop"/></svg><svg width="34" height="30"><use href="#icon-desktop"/></svg></div>
    <div class="slides"><i></i><i class="on"></i><i></i></div>
  </div>
</div>

<!-- ===== Standalone banner 2 ===== -->
<div class="banner" style="top:2290px">
  <div class="hero hero-b">
    <div class="photo photo-white" role="img" aria-label="White shaker kitchen with brass faucet, range hood and fridge"></div>
    <svg class="shapes" viewBox="0 0 1200 363"><circle cx="224" cy="112" r="75" fill="#3a8fdd"/><line x1="360" y1="102" x2="477" y2="102" stroke="#333"/><circle cx="477" cy="102" r="3" fill="#f7a21b"/></svg>
    <div class="copy"><h3>MDF<br>Shaker Doors</h3><p>Timeless &amp; Most Popular Style of Kitchen Doors<br>- Painted or Ready for Painting Options<br>- Short Lead Time</p></div>
    <div class="cta"><span>CHECK THE PRICE</span></div>
    <div class="devices" role="img" aria-label="Order online from phone, laptop or desktop"><svg width="16" height="26"><use href="#icon-phone"/></svg><svg width="36" height="24"><use href="#icon-laptop"/></svg><svg width="34" height="30"><use href="#icon-desktop"/></svg></div>
    <div class="slides" style="right:62px"><i></i><i class="on"></i><i></i></div>
  </div>
</div>

<!-- ===== Standalone banner 3 ===== -->
<div class="banner" style="top:2636px">
  <div class="hero hero-c">
    <div class="photo photo-dark" role="img" aria-label="Modern kitchen with dark wood cabinets, wall ovens and pendant lights"></div>
    <svg class="shapes" viewBox="0 0 1200 363"><polygon points="624,0 810,186 624,372 438,186" fill="#3a8fdd" opacity=".85"/><polygon points="580,-10 770,180 580,370 390,180" fill="none" stroke="#3a8fdd" stroke-width="1.5"/><polygon points="604,2 780,180 604,358 428,180" fill="#fff"/><line x1="290" y1="102" x2="478" y2="102" stroke="#222"/><circle cx="478" cy="102" r="3" fill="#f7a21b"/></svg>
    <div class="copy"><h3>Kitchen<br>Cabinets</h3><p>- Wide Range of Cabinets Designs<br>- Custom Sizes<br>- Great Quality</p></div>
    <div class="cta"><span>CHECK IT OUT</span></div>
    <div class="devices" role="img" aria-label="Order online from phone, laptop or desktop"><svg width="16" height="26"><use href="#icon-phone"/></svg><svg width="36" height="24"><use href="#icon-laptop"/></svg><svg width="34" height="30"><use href="#icon-desktop"/></svg></div>
    <div class="slides"><i></i><i class="on"></i><i></i></div>
  </div>
</div>

</body>
</html>
```